New business card for a regional office of a US M&A company

We need business card for a finance company, office based in Hong Kong , our Head office is in US, our business is to Merge and acquires companies , the new office will be a regional office for the Asia Pacific region. We want to use the head office logo as attached ( but don't have to be exactly the same, can be a variation to it) as a base and then add Asia Pacific alongside the logo.
We would prefer to have be bilingual Eng + Chinese, although we don't really have Chinese company name .

Industry/Entity Type

Business

Contact Information for Business Card

Carla Beth Soren
 

VP,
APAC M&A Operations
Tovar Crest Asia Pacific Limited
 
Unit 1407, K82
27 Sai Lok Fung Road, 
Hong Kong 
 
M: +852 6481 2037
T : +852 2736 4100
F : +852 2736 4155
VOIP: 4813
 
cbsoren@tovarcrest.com

Font styles to use
Serif
Sans Serif

Colors

Designer to choose colors to be used in the design.

Requirements
Must have
• APAC Office

```html
<!DOCTYPE html>
<html lang="en">
<head>
<meta charset="utf-8">
<title>Tovar Crest Asia Pacific – Business Card</title>
<link href="https://fonts.googleapis.com/css2?family=Lato:ital,wght@0,400;0,700;0,900;1,400&display=swap" rel="stylesheet">
<style>
  :root {
    --navy: #10304b;
    --navy-soft: #163a58;
    --cyan: #1fa3d6;
    --paper: #f6f7f8;
    --ink: #1d2b38;
    --ghost: #e3e6ea;
    --stage: #d9dde2;
  }
  * { box-sizing: border-box; margin: 0; padding: 0; }
  html, body { width: 1200px; height: 786px; overflow: hidden; }
  body {
    background: var(--stage);
    font-family: "Lato", sans-serif;
    display: flex;
    align-items: center;
    justify-content: center;
    gap: 60px;
  }
  .card {
    position: relative;
    width: 540px;
    height: 310px;
    clip-path: polygon(0 0, 450px 0, 540px 155px, 450px 310px, 0 310px);
    border-radius: 14px;
  }
  /* front */
  .card--front { background: var(--paper); color: var(--ink); }
  .card__accent { position: absolute; left: 0; top: 0; }
  .contact { position: absolute; left: 38px; top: 34px; }
  .contact__name { font-size: 22px; font-weight: 700; color: var(--navy); letter-spacing: .2px; }
  .contact__title { font-size: 12.5px; font-style: italic; color: var(--cyan); margin-top: 2px; }
  .contact__company { font-size: 12.5px; font-weight: 700; margin-top: 12px; }
  .contact__company .brand { color: var(--cyan); }
  .contact__address { font-size: 12px; line-height: 1.45; margin-top: 3px; }
  .contact__lines { list-style: none; margin-top: 12px; font-size: 12px; line-height: 1.55; }
  .contact__lines li { display: flex; align-items: center; gap: 8px; }
  .contact__lines .label { color: var(--cyan); font-weight: 700; }
  .contact__lines svg { width: 11px; height: 11px; fill: var(--cyan); flex: none; }
  .contact__web { font-weight: 700; }
  .mark-panel {
    position: absolute; right: 30px; top: 60px;
    width: 190px; height: 190px;
    background: var(--ghost);
    display: flex; align-items: center; justify-content: center;
  }
  .mark-panel__inner {
    width: 130px; height: 130px; background: #fff;
    display: flex; flex-direction: column; align-items: center; justify-content: center; gap: 8px;
  }
  .mark-panel__square { width: 30px; height: 30px; background: var(--navy); }
  .mark-panel__name { font-size: 13px; font-weight: 900; color: var(--navy); letter-spacing: 1.5px; }
  /* back */
  .card--back { background: var(--navy); }
  .card__ghost {
    position: absolute; left: 40px; top: 30px;
    width: 170px; height: 130px;
    border: 14px solid var(--navy-soft);
  }
  .brandline {
    position: absolute; right: 120px; bottom: 70px;
    display: flex; align-items: center; gap: 14px;
  }
  .brandline__name {
    font-size: 26px; font-weight: 900; letter-spacing: 2.5px; color: var(--cyan);
    padding-bottom: 6px; border-bottom: 2px solid var(--cyan);
  }
  .brandline__square { width: 24px; height: 24px; border: 3px solid #fff; }
</style>
</head>
<body>
  <article class="card card--front">
    <svg class="card__accent" width="60" height="30" viewBox="0 0 60 30" aria-hidden="true">
      <polygon points="0,0 60,0 30,30 0,30" fill="var(--cyan)"/>
      <polygon points="30,0 60,0 45,18" fill="var(--navy)"/>
    </svg>
    <div class="contact">
      <h1 class="contact__name">Carla Beth Soren</h1>
      <p class="contact__title">VP, APAC M&amp;A Operations</p>
      <p class="contact__company"><span class="brand">Tovar Crest</span> Asia Pacific Limited</p>
      <p class="contact__address">Unit 1407, K82<br>27 Sai Lok Fung Road<br>Hong Kong</p>
      <ul class="contact__lines">
        <li><span class="label">VOIP:</span> 4813</li>
        <li><svg viewBox="0 0 12 12"><rect x="3" y="0" width="6" height="12" rx="1"/></svg>+852 6481 2037</li>
        <li><svg viewBox="0 0 12 12"><path d="M2 1c1 0 2 2 2 3s-1 1-1 2 2 3 3 3 1-1 2-1 3 1 3 2-1 2-2 2C5 12 0 7 0 3 0 2 1 1 2 1z"/></svg>+852 2736 4100</li>
        <li><svg viewBox="0 0 12 12"><rect x="0" y="4" width="12" height="7"/><rect x="3" y="0" width="6" height="4"/></svg>+852 2736 4155</li>
        <li><svg viewBox="0 0 12 12"><path d="M0 2h12v8H0z"/></svg>cbsoren@tovarcrest.com</li>
        <li><svg viewBox="0 0 12 12"><circle cx="6" cy="6" r="5.5"/></svg><span class="contact__web">www.tovarcrest.com</span></li>
      </ul>
    </div>
    <div class="mark-panel">
      <div class="mark-panel__inner">
        <span class="mark-panel__square"></span>
        <span class="mark-panel__name">TOVAR CREST</span>
      </div>
    </div>
  </article>

  <article class="card card--back">
    <div class="card__ghost" aria-hidden="true"></div>
    <div class="brandline">
      <span class="brandline__name">TOVAR CREST</span>
      <span class="brandline__square"></span>
    </div>
  </article>
</body>
</html>
```